#ZELTO

#Zelto is the business name. I need a marketing brochure to show potential clients. The concept is providing the restaurant trade and function centres with volume wine in large wine casks and then on-sell by the glass or in varying carafe sizes. The advantages will be outlined in the file provided I want to introduce the concept and demonstrate the advantages visusally

Restaurant

```html
<!DOCTYPE html>
<html lang="en">
<head>
<meta charset="utf-8">
<title>#Zelto — Brochure Cover</title>
<link rel="stylesheet" href="https://fonts.googleapis.com/css2?family=Playfair+Display:wght@400;900&family=Montserrat:wght@400&display=swap">
<style>
  :root {
    --page-bg: #ffffff;
    --ink-black: #0b0b0b;
    --barrel-dark: #2b1e15;
    --barrel-mid: #5a3f2b;
    --barrel-warm: #7a5a3f;
    --seal-white: #ffffff;
    --title-brown: #3b2a1d;
    --kicker-grey: #cfcfcf;
  }
  html, body {
    margin: 0;
    padding: 0;
    width: 1200px;
    height: 986px;
    overflow: hidden;
    background: var(--page-bg);
  }
  .canvas {
    position: relative;
    width: 1200px;
    height: 986px;
  }
  .brochure {
    position: absolute;
    left: 0;
    top: 0;
    width: 1200px;
    height: 986px;
  }
  .stop-dark { stop-color: var(--barrel-dark); }
  .stop-mid { stop-color: var(--barrel-mid); }
  .stop-warm { stop-color: var(--barrel-warm); }
  .fold-band { fill: var(--ink-black); }
  .seal-circle { fill: var(--seal-white); fill-opacity: 0.78; }
  .footer-dot { fill: var(--seal-white); }
  .cover-title {
    font-family: "Playfair Display", Georgia, serif;
    font-weight: 900;
    font-size: 66px;
    letter-spacing: 4px;
    fill: var(--title-brown);
  }
  .cover-kicker {
    font-family: "Montserrat", Arial, sans-serif;
    font-size: 14px;
    letter-spacing: 4px;
    fill: var(--kicker-grey);
  }
</style>
</head>
<body>
<main class="canvas">
  <svg class="brochure" viewBox="0 0 1200 986" xmlns="http://www.w3.org/2000/svg">
    <defs>
      <linearGradient id="barrel-tones" x1="0" y1="0" x2="0.4" y2="1">
        <stop offset="0" class="stop-dark"/>
        <stop offset="0.45" class="stop-warm"/>
        <stop offset="1" class="stop-mid"/>
      </linearGradient>
      <clipPath id="flap-left"><rect x="227" y="53" width="370" height="880"/></clipPath>
      <clipPath id="flap-right"><rect x="603" y="53" width="370" height="880"/></clipPath>
    </defs>

    <!-- Left flap -->
    <g class="cover-flap cover-flap--left" clip-path="url(#flap-left)">
      <rect class="fold-band" x="227" y="53" width="370" height="880"/>
      <rect x="227" y="53" width="370" height="760" fill="url(#barrel-tones)"
            role="img" aria-label="Photograph of oak wine casks stacked on racks in a cellar"/>
      <circle class="footer-dot" cx="290" cy="930" r="38"/>
      <circle class="footer-dot" cx="390" cy="930" r="38"/>
      <circle class="footer-dot" cx="490" cy="930" r="38"/>
    </g>

    <!-- Right flap -->
    <g class="cover-flap cover-flap--right" clip-path="url(#flap-right)">
      <rect class="fold-band" x="603" y="53" width="370" height="880"/>
      <rect x="603" y="53" width="370" height="760" fill="url(#barrel-tones)"
            role="img" aria-label="Photograph of oak wine casks stacked on racks in a cellar"/>
      <circle class="footer-dot" cx="710" cy="930" r="38"/>
      <circle class="footer-dot" cx="810" cy="930" r="38"/>
      <circle class="footer-dot" cx="910" cy="930" r="38"/>
    </g>

    <!-- Title seal across the fold -->
    <g class="title-seal">
      <circle class="seal-circle" cx="600" cy="330" r="150" clip-path="url(#flap-left)"/>
      <circle class="seal-circle" cx="600" cy="330" r="150" clip-path="url(#flap-right)"/>
      <text class="cover-kicker" x="420" y="215">OUR</text>
      <text class="cover-title" x="600" y="355" text-anchor="middle">#ZELTO</text>
    </g>
  </svg>
</main>
</body>
</html>
```